Dorven Studio 286 the new wave for sound to enlighten open ears

This is a music recording studio, we need pictures of a booth, random pictures of anything that will draw interest to a recording studio, we just need the website to reflect a music studio recording website. Apply generic information on the site that correlates with most music studio websites up to date. We want the modern style look that will entice eyes across the nation. Information should be easily accessible on the website. Dorven Studio 286 is owned by Marcus Tellingworth located 5716 Halberd Ln, Miramar, Fl, 33187. Email: Mtellstudio@veltrox.com and best contact number to date is 612-437-9820. The sound coming out of this location will be radio ready at all times, artist come in one way and come out with more wisdom than before. Its the new way to make music the appropriate way and bring the best out of those willing to reach their peak.

Target Market(s)

Recording Artist

Industry/Entity Type

Recording Studio

Coding

Coded - Design and coding required

Number of Pages Required

1 page

Font styles to use
Sans Serif

Requirements
Must have
• Anything that gives the site a music feel
Nice to have
• microphones, booths, studio mixing desk

```html
<!DOCTYPE html>
<html lang="en">
<head>
<meta charset="utf-8">
<title>Dorven Studio 286</title>
<link rel="stylesheet" href="https://fonts.googleapis.com/css2?family=Open+Sans:wght@400;600;700;800&display=swap">
<style>
:root{
  --red:#ef3b44;
  --red-dark:#d92f38;
  --ink:#222;
  --text:#555;
  --muted:#888;
  --line:#ddd;
  --grey-head:#7a7a7a;
  --footer:#1c1c1c;
  --white:#fff;
}
*{box-sizing:border-box;margin:0;padding:0}
html,body{width:1200px;height:2857px;overflow:hidden}
body{position:relative;font-family:"Open Sans",Arial,sans-serif;color:var(--text);background:var(--white)}
section,header,footer{position:absolute;left:0;width:1200px}
a{color:inherit;text-decoration:none}

/* header */
.site-header{top:0;height:91px;border-top:4px solid var(--red);background:var(--white)}
.brand{position:absolute;left:99px;top:30px;font-size:21px;font-weight:700;color:var(--ink);letter-spacing:.3px;display:flex;align-items:center;gap:12px}
.contact-bar{position:absolute;right:98px;top:10px;display:flex;gap:34px;font-size:15px;color:var(--ink)}
.contact-bar span{display:flex;align-items:center;gap:12px}
.icon-ring{width:30px;height:30px;border-radius:50%;border:1.5px solid var(--red);display:flex;align-items:center;justify-content:center}
.main-nav{position:absolute;right:98px;top:62px;display:flex;gap:28px;font-size:14px;font-weight:600;color:var(--ink);align-items:center}
.main-nav .active{color:var(--red)}

/* hero */
.hero{top:91px;height:444px;overflow:hidden}
.hero-photo{position:absolute;inset:0;background:
  radial-gradient(ellipse at 20% 30%,rgba(230,40,50,.75),transparent 55%),
  radial-gradient(ellipse at 80% 25%,rgba(120,60,200,.75),transparent 55%),
  radial-gradient(ellipse at 50% 85%,#888 0,#3a3a44 60%),
  linear-gradient(90deg,#c02030,#5b3fa8,#6a2a90)}
.hero-copy{position:absolute;left:0;right:0;top:132px;text-align:center;color:var(--white)}
.hero-copy h1{font-size:62px;font-weight:800;letter-spacing:1px;line-height:1}
.hero-copy p{font-size:27px;margin-top:14px}
.btn-solid{display:inline-block;margin-top:16px;background:var(--red);color:var(--white);font-size:14px;font-weight:700;padding:9px 22px;border:1px solid #fff}
.slider-dots{position:absolute;left:530px;top:393px;display:flex;gap:8px}
.slider-dots i{display:block;width:30px;height:4px;background:var(--white)}
.slider-dots i:first-child{background:var(--red)}

/* welcome */
.welcome{top:535px;height:305px;text-align:center}
.section-title{font-size:26px;font-weight:700;color:var(--ink);text-align:center}
.welcome .section-title{margin-top:56px}
.welcome p{width:760px;margin:26px auto 0;font-size:13px;line-height:24px;color:var(--muted)}
.btn-outline{display:inline-block;border:1.5px solid #999;color:var(--red);font-size:13px;font-weight:700;padding:11px 22px;background:var(--white)}
.welcome .btn-outline{margin-top:30px}
.divider{position:absolute;left:99px;width:1002px;top:302px;height:1px;background:var(--line)}

/* albums */
.albums{top:840px;height:505px}
.albums .section-title{margin-top:44px}
.album-row{position:absolute;top:111px;left:97px;display:flex;gap:15px}
.album-card{width:240px;height:362px;border:1px solid var(--line);position:relative;overflow:hidden;background:var(--white)}
.album-art{height:213px}
.art-1{background:linear-gradient(135deg,#2b3340,#5a6a78,#1b1f26)}
.art-2{background:linear-gradient(135deg,#e9e9e9,#8a8a8a,#3a3a3a)}
.art-3{background:linear-gradient(135deg,#b58a6a,#6d5a55,#d9d0c8)}
.art-4{background:linear-gradient(90deg,#c21e8e,#e8327a,#f16a2a,#f5c31e)}
.ribbon{position:absolute;left:0;top:0;width:0;height:0;border-top:52px solid var(--red);border-right:52px solid transparent}
.ribbon span{position:absolute;left:2px;top:-44px;transform:rotate(-45deg);color:#fff;font-size:11px;font-weight:700}
.album-body{padding:16px 20px}
.album-body h3{font-size:16px;font-weight:600;color:var(--ink)}
.album-body p{font-size:12px;line-height:20px;color:var(--muted);margin-top:6px}
.album-foot{display:flex;justify-content:space-between;align-items:center;margin-top:14px}
.hear{font-size:12px;font-weight:700;color:var(--red)}
.duration{background:#9a9a9a;color:#fff;font-size:11px;padding:6px 10px;display:flex;align-items:center;gap:6px}
.arrow{position:absolute;top:260px}

/* services */
.services{top:1375px;height:307px;display:flex}
.service{width:300px;height:307px;position:relative;color:#fff;text-align:center}
.svc-1{background:linear-gradient(160deg,#243a66,#0e1b36)}
.svc-2{background:linear-gradient(160deg,#e5a816,#b47c08)}
.svc-3{background:linear-gradient(160deg,#1e9aa8,#0d6470)}
.svc-4{background:linear-gradient(160deg,#c79a6e,#7a5838)}
.service svg{position:absolute;left:110px;top:90px}
.service h3{position:absolute;left:0;right:0;top:197px;font-size:20px;font-weight:700}

/* pricing */
.pricing{top:1682px;height:558px}
.pricing .section-title{margin-top:60px}
.plan-row{position:absolute;top:124px;left:97px;display:flex;gap:17px}
.plan{position:relative;width:324px;height:366px;border:1px solid var(--line);box-shadow:0 1px 4px rgba(0,0,0,.12);background:#fff}
.plan h3{height:42px;line-height:42px;background:var(--grey-head);color:#fff;font-size:20px;font-weight:600;text-align:center}
.plan.featured h3{background:var(--red)}
.plan ul{list-style:none;padding:26px 14px 0 18px}
.plan li{display:flex;align-items:flex-start;font-size:12px;color:var(--muted);line-height:22px;margin-bottom:24px}
.plan li .tick{flex:none;margin-top:4px;margin-right:10px}
.plan li b{flex:none;width:50px;color:var(--ink);font-weight:700;font-size:13px}
.plan li span{flex:1}
.plan .btn-outline{position:absolute;left:50%;transform:translateX(-50%);bottom:28px;font-size:13px;padding:10px 24px}

/* counters */
.counters{top:2240px;height:309px;color:#fff;text-align:center}
.counters-photo{position:absolute;inset:0;background:linear-gradient(120deg,#f04652,#e0303c 50%,#f07078)}
.counter{position:absolute;top:40px;width:300px}
.counter .ring{width:136px;height:136px;border:2px solid #fff;border-radius:50%;margin:0 auto;display:flex;align-items:center;justify-content:center}
.counter strong{display:block;font-size:36px;font-weight:800;margin-top:16px;line-height:1}
.counter span{font-size:20px}

/* footer */
.site-footer{top:2549px;height:308px;background:var(--footer);color:#ccc}
.site-footer .brand{left:82px;top:121px;color:#fff}
.f-col{position:absolute;top:42px}
.f-col h4{font-size:17px;font-weight:600;color:#fff;margin-bottom:14px}
.f-col li{list-style:none;font-size:12px;line-height:22px}
.f-col p{font-size:12px;line-height:21px}
.email-field{margin-top:14px;width:255px;height:36px;background:#fff;color:#aaa;font-size:11px;padding:11px 12px}
.btn-sub{display:inline-block;margin-top:16px;background:var(--red);color:#fff;font-size:11px;font-weight:600;padding:6px 10px}
.f-contact li{display:flex;gap:14px;margin-bottom:18px;line-height:20px}
.copyright{position:absolute;left:99px;top:260px;font-size:12px;color:#bbb}
.socials{position:absolute;left:958px;top:249px;display:flex;gap:6px}
.socials i{width:30px;height:30px;border-radius:50%;display:block}
</style>
</head>
<body>

<header class="site-header">
  <div class="brand">Dorven Studio 286</div>
  <div class="contact-bar">
    <span><i class="icon-ring"><svg width="14" height="14" viewBox="0 0 24 24"><path fill="#ef3b44" d="M6.6 10.8a15.1 15.1 0 0 0 6.6 6.6l2.2-2.2c.3-.3.7-.4 1-.2 1.1.4 2.3.6 3.6.6.6 0 1 .4 1 1V20c0 .6-.4 1-1 1A17 17 0 0 1 3 4c0-.6.4-1 1-1h3.5c.6 0 1 .4 1 1 0 1.3.2 2.5.6 3.6.1.3 0 .7-.2 1z"/></svg></i>612-437-9820</span>
    <span><i class="icon-ring"><svg width="14" height="14" viewBox="0 0 24 24"><path fill="#ef3b44" d="M2 5h20v14H2zm2 2v.5l8 5 8-5V7l-8 5z"/></svg></i>Mtellstudio@veltrox.com</span>
  </div>
  <nav class="main-nav">
    <a class="active">HOME</a><a>ABOUT</a><a>MIX/MASTERING SERVICES</a><a>MUSIC MERCH</a><a>BLOG</a><a>CONTACT</a>
    <svg width="14" height="14" viewBox="0 0 24 24"><circle cx="10" cy="10" r="7" fill="none" stroke="#222" stroke-width="3"/><path d="M15 15l7 7" stroke="#222" stroke-width="3"/></svg>
  </nav>
</header>

<section class="hero">
  <div class="hero-photo" role="img" aria-label="Recording studio control room with mixing console and monitors under colourful lights"></div>
  <div class="hero-copy">
    <h1>DORVEN STUDIO 286</h1>
    <p>We are a music recording studio</p>
    <a class="btn-solid">GET FREE PROPOSALS</a>
  </div>
  <div class="slider-dots"><i></i><i></i><i></i><i></i></div>
</section>

<section class="welcome">
  <h2 class="section-title">WELCOME TO DORVEN STUDIO 286</h2>
  <p>At vero eos et accusamus et iusto odio dignissimos ducimus qui blanditiis praesentium voluptatum deleniti atque corrupti os dolores et quas molestias excepturi sint occaecati cupiditate non provident, similique sunt in culpa qui officia deserunt mollit ia animi, id est laborum et dolorum fuga. Et harum quidem rerum facilis est et expedita distinctio.</p>
  <a class="btn-outline">GET AWESOME SOUNDING TRACKS</a>
  <div class="divider"></div>
</section>

<section class="albums">
  <h2 class="section-title">FEATURED ALBUMS</h2>
  <svg class="arrow" style="left:52px" width="14" height="26" viewBox="0 0 14 26"><path d="M12 2L2 13l10 11" fill="none" stroke="#bbb" stroke-width="2"/></svg>
  <svg class="arrow" style="left:1134px" width="14" height="26" viewBox="0 0 14 26"><path d="M2 2l10 11L2 24" fill="none" stroke="#bbb" stroke-width="2"/></svg>
  <div class="album-row">
    <article class="album-card">
      <div class="album-art art-1" role="img" aria-label="Engineer working at a mixing desk"></div>
      <div class="ribbon"><span>NEW</span></div>
      <div class="album-body"><h3>At vero eos et accus</h3><p>At vero eos et accusamus et iustood io dignissimos ducimus.</p>
        <div class="album-foot"><a class="hear">HEAR MORE &gt;&gt;</a><span class="duration">&#9719; 0:30 SEC</span></div></div>
    </article>
    <article class="album-card">
      <div class="album-art art-2" role="img" aria-label="Headphones resting on a mixing console"></div>
      <div class="ribbon"><span>NEW</span></div>
      <div class="album-body"><h3>At vero eos et accus</h3><p>At vero eos et accusamus et iustood io dignissimos ducimus.</p>
        <div class="album-foot"><a class="hear">HEAR MORE &gt;&gt;</a><span class="duration">&#9719; 0:30 SEC</span></div></div>
    </article>
    <article class="album-card">
      <div class="album-art art-3" role="img" aria-label="Two singers recording at a microphone in a booth"></div>
      <div class="ribbon"><span>NEW</span></div>
      <div class="album-body"><h3>At vero eos et accus</h3><p>At vero eos et accusamus et iustood io dignissimos ducimus.</p>
        <div class="album-foot"><a class="hear">HEAR MORE &gt;&gt;</a><span class="duration">&#9719; 0:30 SEC</span></div></div>
    </article>
    <article class="album-card">
      <div class="album-art art-4" role="img" aria-label="Colourful audio equaliser bars"></div>
      <div class="ribbon"><span>NEW</span></div>
      <div class="album-body"><h3>At vero eos et accus</h3><p>At vero eos et accusamus et iustood io dignissimos ducimus.</p>
        <div class="album-foot"><a class="hear">HEAR MORE &gt;&gt;</a><span class="duration">&#9719; 0:30 SEC</span></div></div>
    </article>
  </div>
</section>

<section class="services">
  <div class="service svc-1" role="img" aria-label="DJ at a mixing deck, blue tint">
    <svg width="80" height="80" viewBox="0 0 80 80"><circle cx="40" cy="40" r="34" fill="none" stroke="#fff" stroke-width="5"/><circle cx="40" cy="40" r="8" fill="#fff"/><path d="M56 20l6 30-10 8" fill="none" stroke="#fff" stroke-width="4"/></svg>
    <h3>RECORDING MIXING</h3>
  </div>
  <div class="service svc-2" role="img" aria-label="Microphone over a mixer, yellow tint">
    <svg width="80" height="80" viewBox="0 0 80 80"><circle cx="40" cy="14" r="6" fill="#fff"/><path d="M40 22v16M22 14l18 18 18-18" stroke="#fff" stroke-width="5" fill="none"/><rect x="8" y="44" width="64" height="30" rx="4" fill="none" stroke="#fff" stroke-width="4"/><circle cx="26" cy="59" r="7" fill="#fff"/><circle cx="54" cy="59" r="7" fill="#fff"/></svg>
    <h3>PARTIES</h3>
  </div>
  <div class="service svc-3" role="img" aria-label="Mixing console faders, teal tint">
    <svg width="80" height="80" viewBox="0 0 80 80"><rect x="24" y="6" width="32" height="68" rx="3" fill="none" stroke="#fff" stroke-width="4"/><circle cx="40" cy="20" r="5" fill="#fff"/><circle cx="40" cy="50" r="12" fill="none" stroke="#fff" stroke-width="4"/><path d="M14 28a22 22 0 0 0 0 30M66 28a22 22 0 0 1 0 30" fill="none" stroke="#fff" stroke-width="3"/></svg>
    <h3>PRODUCTION BEATS</h3>
  </div>
  <div class="service svc-4" role="img" aria-label="Singer with headphones in a vocal booth, sepia tint">
    <svg width="80" height="80" viewBox="0 0 80 80"><rect x="12" y="6" width="56" height="68" rx="3" fill="none" stroke="#fff" stroke-width="4"/><path d="M22 22h36M22 40h36M22 58h36" stroke="#fff" stroke-width="3"/><rect x="28" y="16" width="8" height="12" fill="#fff"/><rect x="44" y="34" width="8" height="12" fill="#fff"/><rect x="32" y="52" width="8" height="12" fill="#fff"/></svg>
    <h3>MUSIC LESSONS</h3>
  </div>
</section>

<section class="pricing">
  <h2 class="section-title">PRICING PLAN</h2>
  <div class="plan-row">
    <div class="plan">
      <h3>Recording Price</h3>
      <ul>
        <li><svg class="tick" width="14" height="14" viewBox="0 0 14 14"><circle cx="7" cy="7" r="7" fill="#ef3b44"/><path d="M4 7l2 2 4-4" stroke="#fff" stroke-width="2" fill="none"/></svg><b>$80</b><span>per hour minimum 4 hours required</span></li>
        <li><svg class="tick" width="14" height="14" viewBox="0 0 14 14"><circle cx="7" cy="7" r="7" fill="#ef3b44"/><path d="M4 7l2 2 4-4" stroke="#fff" stroke-width="2" fill="none"/></svg><b>75$</b><span>per hour minimum 8 hours required</span></li>
        <li><svg class="tick" width="14" height="14" viewBox="0 0 14 14"><circle cx="7" cy="7" r="7" fill="#ef3b44"/><path d="M4 7l2 2 4-4" stroke="#fff" stroke-width="2" fill="none"/></svg><b>$70</b><span>per hour minimum 12 hours required</span></li>
        <li><svg class="tick" width="14" height="14" viewBox="0 0 14 14"><circle cx="7" cy="7" r="7" fill="#ef3b44"/><path d="M4 7l2 2 4-4" stroke="#fff" stroke-width="2" fill="none"/></svg><b>$90</b><span>for individual hours, packages recommended</span></li>
      </ul>
      <a class="btn-outline">SUBSCRIBE</a>
    </div>
    <div class="plan featured">
      <h3>Memberships Deals</h3>
      <ul>
        <li><svg class="tick" width="14" height="14" viewBox="0 0 14 14"><circle cx="7" cy="7" r="7" fill="#ef3b44"/><path d="M4 7l2 2 4-4" stroke="#fff" stroke-width="2" fill="none"/></svg><b>$1500</b><span>get 48 recording hours in addition to 24 hours mix down</span></li>
        <li><svg class="tick" width="14" height="14" viewBox="0 0 14 14"><circle cx="7" cy="7" r="7" fill="#ef3b44"/><path d="M4 7l2 2 4-4" stroke="#fff" stroke-width="2" fill="none"/></svg><b>$2500</b><span>get 72 recording hours in addition to 48 hours mix down</span></li>
        <li><svg class="tick" width="14" height="14" viewBox="0 0 14 14"><circle cx="7" cy="7" r="7" fill="#ef3b44"/><path d="M4 7l2 2 4-4" stroke="#fff" stroke-width="2" fill="none"/></svg><b>$3500</b><span>get 96 recording hours in addition to 72 hours mix down</span></li>
      </ul>
      <a class="btn-outline">SUBSCRIBE</a>
    </div>
    <div class="plan">
      <h3>Mix down only prices</h3>
      <ul>
        <li><svg class="tick" width="14" height="14" viewBox="0 0 14 14"><circle cx="7" cy="7" r="7" fill="#ef3b44"/><path d="M4 7l2 2 4-4" stroke="#fff" stroke-width="2" fill="none"/></svg><b>$50</b><span>per hour minimum 4 hours required</span></li>
        <li><svg class="tick" width="14" height="14" viewBox="0 0 14 14"><circle cx="7" cy="7" r="7" fill="#ef3b44"/><path d="M4 7l2 2 4-4" stroke="#fff" stroke-width="2" fill="none"/></svg><b>$45</b><span>per hour minimum 8 hours required</span></li>
        <li><svg class="tick" width="14" height="14" viewBox="0 0 14 14"><circle cx="7" cy="7" r="7" fill="#ef3b44"/><path d="M4 7l2 2 4-4" stroke="#fff" stroke-width="2" fill="none"/></svg><b>$40</b><span>per hour minimum 12 hours required</span></li>
        <li><svg class="tick" width="14" height="14" viewBox="0 0 14 14"><circle cx="7" cy="7" r="7" fill="#ef3b44"/><path d="M4 7l2 2 4-4" stroke="#fff" stroke-width="2" fill="none"/></svg><b>$60</b><span>for individual hours, packages recommended</span></li>
      </ul>
      <a class="btn-outline">SUBSCRIBE</a>
    </div>
  </div>
</section>

<section class="counters">
  <div class="counters-photo" role="img" aria-label="Close-up of a mixing console with red overlay"></div>
  <div class="counter" style="left:142px">
    <div class="ring"><svg width="84" height="50" viewBox="0 0 84 50"><path d="M4 25C18 6 66 6 80 25 66 44 18 44 4 25z" fill="none" stroke="#fff" stroke-width="5"/><circle cx="42" cy="25" r="12" fill="#fff"/></svg></div>
    <strong>25489</strong><span>Visitors Counter</span>
  </div>
  <div class="counter" style="left:450px">
    <div class="ring"><svg width="60" height="66" viewBox="0 0 60 66"><path d="M18 52V10l38-8v42" fill="none" stroke="#fff" stroke-width="6"/><ellipse cx="11" cy="53" rx="10" ry="8" fill="#fff"/><ellipse cx="49" cy="45" rx="10" ry="8" fill="#fff"/></svg></div>
    <strong>12589</strong><span>Beats Counter</span>
  </div>
  <div class="counter" style="left:785px">
    <div class="ring"><svg width="76" height="66" viewBox="0 0 76 66"><circle cx="28" cy="38" r="17" fill="none" stroke="#fff" stroke-width="10" stroke-dasharray="6 4.6"/><circle cx="28" cy="38" r="9" fill="none" stroke="#fff" stroke-width="5"/><circle cx="58" cy="16" r="10" fill="none" stroke="#fff" stroke-width="6" stroke-dasharray="4 3.8"/><circle cx="58" cy="50" r="8" fill="none" stroke="#fff" stroke-width="5" stroke-dasharray="3.5 3"/></svg></div>
    <strong>21894</strong><span>Mix/Mastering Projects</span>
  </div>
</section>

<footer class="site-footer">
  <div class="brand">Dorven Studio 286</div>
  <div class="f-col" style="left:432px">
    <h4>Information</h4>
    <ul><li>Home</li><li>About</li><li>Mix/Mastering Services</li><li>Music Merch</li><li>Blog</li><li>Contact</li></ul>
  </div>
  <div class="f-col" style="left:623px">
    <h4>Newsletter Subscription</h4>
    <p>Register your Email Address to Receive a<br>Free Lease! Terms Apply.</p>
    <div class="email-field">Email Address</div>
    <a class="btn-sub">SUBSCRIBE</a>
  </div>
  <div class="f-col f-contact" style="left:939px">
    <h4>Contact Us</h4>
    <ul>
      <li><svg width="12" height="16" viewBox="0 0 12 16"><path d="M6 0a6 6 0 0 1 6 6c0 4-6 10-6 10S0 10 0 6a6 6 0 0 1 6-6z" fill="#fff"/><circle cx="6" cy="6" r="2" fill="#1c1c1c"/></svg><span>5716 Halberd Ln, Miramar,<br>Fl, 33187</span></li>
      <li><svg width="12" height="14" viewBox="0 0 24 24"><path fill="#fff" d="M6.6 10.8a15.1 15.1 0 0 0 6.6 6.6l2.2-2.2c.3-.3.7-.4 1-.2 1.1.4 2.3.6 3.6.6.6 0 1 .4 1 1V20c0 .6-.4 1-1 1A17 17 0 0 1 3 4c0-.6.4-1 1-1h3.5c.6 0 1 .4 1 1 0 1.3.2 2.5.6 3.6.1.3 0 .7-.2 1z"/></svg><span>612-437-9820</span></li>
      <li><svg width="14" height="14" viewBox="0 0 24 24"><path fill="#fff" d="M2 5h20v14H2zm2 2v.5l8 5 8-5V7l-8 5z"/></svg><span>Mtellstudio@veltrox.com</span></li>
    </ul>
  </div>
  <p class="copyright">Copyright © 2017, Dorven Studio 286. All rights reserved. Privacy Policy &nbsp;|&nbsp; Terms of Service.</p>
  <div class="socials"><i style="background:#3b5a9a"></i><i style="background:#2aa3ef"></i><i style="background:#d62d2d"></i><i style="background:#e04a3a"></i></div>
</footer>

</body>
</html>
```